Freelancers in the field of IT security and IT service need a business card design

I need a business card design for my company. I am a freelancer and active in the area of IT security, IT support% 26 # 252; tung, consulting. I am not yet color-coded, but it should be a modern color that can also be used for a later website. The design should be innovation. Exude dynamism and reliability

Target Market(s)

IT security, IT solutions

Contact Information for Business Card

Firma: brunov-consulting, Inhaber: Lukas Brunov
Adresse: Lindenhof 4, D-73618 Talbrunn
Telefon: +49 (0) 5137 640928
E-Mail Lukas.Brunov@brunov-consulting.example

```html
<!DOCTYPE html>
<html lang="de">
<head>
<meta charset="utf-8">
<title>brunov-consulting – Visitenkarte</title>
<link href="https://fonts.googleapis.com/css2?family=Roboto+Condensed:wght@400&family=Roboto:wght@300&display=swap" rel="stylesheet">
<style>
  :root {
    --stage: #e4e6e9;
    --card-dark: #2b2c30;
    --card-light: #4a4c51;
    --accent: #4fa3dc;
    --text-light: #f1f2f4;
    --text-muted: #e2e4e7;
  }
  * { margin: 0; padding: 0; box-sizing: border-box; }
  html, body {
    width: 1200px; height: 936px; overflow: hidden;
    background: var(--stage);
  }
  .business-card {
    position: absolute; left: 100px; top: 168px;
    width: 1000px; height: 600px;
    background:
      radial-gradient(ellipse 70% 45% at 50% 52%, var(--card-light) 0%, rgba(74,76,81,0) 100%),
      linear-gradient(180deg, #242528 0%, #3a3c40 55%, #2e2f33 100%);
    border-left: 4px solid var(--accent);
    border-bottom: 4px solid var(--accent);
    box-shadow: 0 10px 30px rgba(0,0,0,.18);
    font-family: "Roboto Condensed", sans-serif;
  }
  .brand {
    position: absolute; left: 60px; top: 200px; width: 440px;
    text-align: center;
  }
  .brand-mark {
    display: block; margin: 0 auto 34px;
    width: 110px; height: 110px; border-radius: 50%;
    border: 5px solid var(--accent);
  }
  .brand-name {
    color: var(--text-light);
    font-size: 34px; font-weight: 400;
    letter-spacing: 4px; text-transform: uppercase;
    white-space: nowrap;
  }
  .divider {
    position: absolute; left: 506px; width: 2px;
    background: var(--accent);
  }
  .divider--name { top: 198px; height: 70px; }
  .divider--contact { top: 307px; height: 101px; }
  .person-name {
    position: absolute; left: 539px; top: 186px;
    font-family: "Roboto", sans-serif; font-weight: 300;
    font-size: 44px; color: var(--accent); letter-spacing: -0.5px;
    text-transform: uppercase; white-space: nowrap;
  }
  .person-role {
    position: absolute; left: 539px; top: 243px;
    font-size: 25px; color: var(--text-muted);
  }
  .contact-list { list-style: none; position: absolute; left: 539px; top: 305px; }
  .contact-item {
    display: flex; align-items: center; height: 37px;
    font-size: 23px; color: var(--text-muted); white-space: nowrap;
  }
  .contact-icon {
    width: 24px; height: 24px; margin-right: 12px; flex: none;
    fill: none; stroke: var(--accent); stroke-width: 1.6;
    stroke-linecap: round; stroke-linejoin: round;
  }
</style>
</head>
<body>
  <div class="business-card">
    <div class="brand">
      <span class="brand-mark"></span>
      <div class="brand-name">brunov-consulting</div>
    </div>

    <span class="divider divider--name"></span>
    <div class="person-name">Lukas Brunov</div>
    <div class="person-role">Founder</div>

    <span class="divider divider--contact"></span>
    <ul class="contact-list">
      <li class="contact-item">
        <svg class="contact-icon" viewBox="0 0 24 24" aria-hidden="true">
          <circle cx="12" cy="12" r="10"/>
          <path d="M8.5 7.5c.6-.6 1.3-.5 1.6.1l.8 1.5c.2.5.1 1-.3 1.3l-.5.4c.6 1.4 1.6 2.4 3 3l.4-.5c.3-.4.8-.5 1.3-.3l1.5.8c.6.3.7 1 .1 1.6-.9.9-2.2 1.1-3.4.5-2.2-1.1-3.9-2.8-5-5-.6-1.2-.4-2.5.5-3.4z"/>
        </svg>
        +49 (0) 5137 640928
      </li>
      <li class="contact-item">
        <svg class="contact-icon" viewBox="0 0 24 24" aria-hidden="true">
          <rect x="2.5" y="5.5" width="19" height="13"/>
          <path d="M2.5 5.5l9.5 7.5 9.5-7.5M2.5 18.5l7-6.5M21.5 18.5l-7-6.5"/>
        </svg>
        Lukas.Brunov@brunov-consulting.example
      </li>
      <li class="contact-item">
        <svg class="contact-icon" viewBox="0 0 24 24" aria-hidden="true">
          <path d="M12 22s-7-7.2-7-12.5a7 7 0 0 1 14 0C19 14.8 12 22 12 22z"/>
          <circle cx="12" cy="9.5" r="2.6"/>
        </svg>
        Lindenhof 4, D-73618 Talbrunn
      </li>
    </ul>
  </div>
</body>
</html>
```